Membership Flyer Design Project

We need a one page double sided 8.5x11 inch flyer to promote membership in our professional association serving human resource professionals in Southern California. the association is dedicated to the continuous enhancement of human resources through networking, learning, and advocacy.

PRIMARY COLORS

NAVY
PANTONE® 282 C
RGB: 00, 33, 71 / HTML: 002147
CMYK: 100, 68, 00, 54

OPAQUE WHITE
RGB: 255, 255, 255 / HTML: FFFFFF
CMYK: 00, 00, 00, 00

GOLD
PANTONE® 1235 C
RGB: 255, 182, 18 / HTML: FFB612
CMYK: 00, 29, 91, 00

SECONDARY COLORS

RED
PANTONE® 186 C
RGB: 198, 12, 48 / HTML: C60C30
CMYK: 00, 100, 81, 04

LIGHT BLUE
PANTONE® 279 C
RGB: 75, 146, 219 / HTML: 4B92DB
CMYK: 68, 34, 00, 00

GREY
PANTONE® 429 C
RGB: 165, 172, 175 / HTML A5ACAF
CMYK: 03, 00, 00, 32

Target Market(s)

The demographics of our prospect audience is 65+% female, 60% 30-50 years old, and 90% from Southern California.

Industry/Entity Type

Learning

Requirements
Must have
• #1 WSGP logo (attached)
#2 Affiliate of CSLP logo (attached)
#3 contact information

Workforce Stewards Guild of the Pacific (WSGP)
742 W Marlowe Ave, Ste 1180
El Segundo, CA 90245
+1 (310) 555-0187
Fax +1 (310) 555-0164
www.wsgpguild.example

#4 About WSGP
The Workforce Stewards Guild of the Pacific (WSGP) is the largest affiliate chapter of the Council for Staffing Leadership Practice (CSLP). Representing more than 3,500 individual members from over 2,500 companies, WSGP is organized into 16 locations, serving communities in Los Angeles, Orange, Riverside, San Bernardino and Ventura counties. Founded in 1944, WSGP is dedicated to the continuous enhancement of human resources through networking learning and advocacy.

#5 call to action ribbon/banner
Not A Member Yet? Sign Up Now! wsgpguild.example/join

#Exclusive Member Benefits
Special rates to local, regional, and state programs ($615 value)
Complementary monthly webinars ($588 value)
RuleDesk weekly briefing, forms, policies, and checklists ($195 value)
Workplace Statute Callbox ($399 value)
WSGPeBrief newsletter ($35 value)
Access to Linkfolio and listserv groups
Special discounts from 5% to 15% of affinity partners' products and services

#6 Annual Member Dues
$150 to join
$125 to renew

#7 insert three images
diverse group of business people attending a seminar/conference
diverse group of people networking in a non-business setting
California state capital building

#8 Locations:
wsgpguild.example/locations

Anaheim
Burbank
Camarillo
Irvine
Los Angeles (downtown)
Long Beach
Manhattan Beach
Palmdale
Palm Desert
Pasadena
Pomona
Riverside
Santa Clarita
Santa Monica
Temecula
Woodland Hills

#Social Media icons:
Facebook
Linkfolio
Twitter
YouTube
Pinterest

```html
<!DOCTYPE html>
<html lang="en">
<head>
<meta charset="utf-8">
<title>WSGP Membership Flyer – Member Benefits</title>
<link href="https://fonts.googleapis.com/css2?family=Oswald:wght@500;600;700&family=Arimo:wght@400;700&display=swap" rel="stylesheet">
<style>
  :root {
    --navy: #002147;
    --navy-line: #3a5275;
    --gold: #ffb612;
    --white: #ffffff;
    --red: #c60c30;
    --grey: #c9cdd1;
    --grey-light: #d6d9dc;
  }
  * { margin: 0; padding: 0; box-sizing: border-box; }
  html, body { width: 927px; height: 1200px; overflow: hidden; }
  body { font-family: "Arimo", Arial, sans-serif; background: var(--grey); }

  .flyer { position: relative; width: 927px; height: 1200px; overflow: hidden; background: var(--grey); }
  .backdrop { position: absolute; inset: 0; }

  .capitol-art {
    position: absolute; left: 470px; top: 690px; width: 390px; height: 510px;
    background: radial-gradient(ellipse at 50% 40%, var(--grey-light) 0%, rgba(214,217,220,0.5) 55%, rgba(201,205,209,0) 80%);
  }

  .benefits-title {
    position: absolute; left: 79px; top: 122px;
    font-family: "Oswald", "Arial Narrow", sans-serif; font-weight: 600;
    font-size: 43px; letter-spacing: 0.3px; color: var(--gold);
  }

  .benefit-list { position: absolute; left: 74px; top: 196px; width: 410px; list-style: none; }
  .benefit {
    display: flex; align-items: center; height: 97px;
    border-bottom: 1.5px solid var(--navy-line);
  }
  .benefit:last-child { border-bottom: none; }
  .benefit-value {
    width: 116px; flex: none; text-align: right; padding-right: 14px;
    font-family: "Oswald", "Arial Narrow", sans-serif; font-weight: 700;
    color: var(--gold); line-height: 1;
  }
  .benefit-value .amount { font-size: 50px; display: block; }
  .benefit-value .amount .sign { font-size: 58px; vertical-align: -4px; }
  .benefit-value .label {
    display: block; margin-top: -4px; font-family: "Arimo", Arial, sans-serif;
    font-weight: 400; font-size: 14px; color: var(--white);
  }
  .benefit-text { color: var(--white); font-size: 17.5px; line-height: 1.3; }
  .benefit.short .benefit-value { width: 150px; }

  .dues-card {
    position: absolute; left: 508px; top: 196px; width: 344px; height: 448px;
    background: var(--gold); border: 3px solid var(--white); border-radius: 20px;
    color: var(--white); padding: 22px 0 0 20px;
  }
  .perks { font-size: 26px; line-height: 1.22; }
  .perks .range { display: block; font-weight: 700; font-size: 50px; line-height: 1.05; }
  .dues-divider { border: none; border-top: 2px solid var(--white); margin: 22px 0 0 -20px; width: 341px; }
  .dues-title { font-size: 27px; margin-top: 20px; }
  .dues-options { display: flex; margin-top: 10px; }
  .dues-option { width: 165px; }
  .dues-option .price { display: block; font-weight: 700; font-size: 48px; line-height: 1; }
  .dues-option .term { display: block; font-size: 25px; margin-top: 4px; }

  .about { position: absolute; left: 55px; top: 815px; width: 390px; color: var(--navy); }
  .about h2 { font-size: 23px; font-weight: 700; margin-bottom: 10px; }
  .about p { font-size: 15.3px; font-weight: 700; line-height: 22.5px; }

  .locations { position: absolute; left: 485px; top: 845px; color: var(--navy); }
  .locations h2 { font-size: 22.5px; font-weight: 700; letter-spacing: -0.2px; }
  .location-list {
    list-style: none; margin-top: 18px; display: grid;
    grid-template-columns: 254px 180px; grid-auto-flow: column; grid-template-rows: repeat(8, 30.3px);
  }
  .location-list li { font-size: 16.5px; font-weight: 700; display: flex; align-items: center; }
  .location-list li::before {
    content: ""; width: 8px; height: 8px; background: var(--red); margin-right: 12px; flex: none;
  }
</style>
</head>
<body>
<div class="flyer">
  <svg class="backdrop" width="927" height="1200" viewBox="0 0 927 1200" aria-hidden="true">
    <rect width="927" height="1200" fill="#c9cdd1"/>
    <path d="M0 0 H927 V600 C700 640 300 660 0 752 Z" fill="#002147"/>
    <path d="M0 752 C300 660 700 640 927 600 V624 C690 660 330 690 0 772 Z" fill="#ffffff"/>
  </svg>

  <div class="capitol-art" role="img" aria-label="Faint illustration of the California state capitol building"></div>

  <h1 class="benefits-title">Exclusive Member Benefits</h1>

  <ul class="benefit-list">
    <li class="benefit">
      <div class="benefit-value"><span class="amount"><span class="sign">$</span>615</span><span class="label">value</span></div>
      <div class="benefit-text">Special rates to local, regional,<br>and state programs</div>
    </li>
    <li class="benefit">
      <div class="benefit-value"><span class="amount"><span class="sign">$</span>588</span><span class="label">value</span></div>
      <div class="benefit-text">Complementary monthly<br>webinars</div>
    </li>
    <li class="benefit">
      <div class="benefit-value"><span class="amount"><span class="sign">$</span>195</span><span class="label">value</span></div>
      <div class="benefit-text">RuleDesk weekly briefing,<br>forms, policies, and checklists</div>
    </li>
    <li class="benefit">
      <div class="benefit-value"><span class="amount"><span class="sign">$</span>399</span><span class="label">value</span></div>
      <div class="benefit-text">Workplace Statute<br>Callbox</div>
    </li>
    <li class="benefit short">
      <div class="benefit-value"><span class="amount"><span class="sign">$</span>35</span><span class="label">value</span></div>
      <div class="benefit-text">WSGPeBrief<br>newsletter</div>
    </li>
  </ul>

  <aside class="dues-card">
    <p class="perks">Access to Linkfolio<br>and listserv groups<br>Special discounts<span class="range">5% to 15%</span>of affinity partners’<br>products and services</p>
    <hr class="dues-divider">
    <p class="dues-title">Annual Member Dues</p>
    <div class="dues-options">
      <p class="dues-option"><span class="price">$150</span><span class="term">to join</span></p>
      <p class="dues-option"><span class="price">$125</span><span class="term">to renew</span></p>
    </div>
  </aside>

  <section class="about">
    <h2>About Us</h2>
    <p>The Workforce Stewards Guild of the Pacific (WSGP) is the largest affiliate chapter of the Council for Staffing Leadership Practice (CSLP). Representing more than 3,500 individual members from over 2,500 companies, WSGP is organized into 16 locations, serving communities in Los Angeles, Orange, Riverside, San Bernardino and Ventura counties. Founded in 1944, WSGP is dedicated to the continuous enhancement of human resources through networking learning and advocacy.</p>
  </section>

  <section class="locations">
    <h2>wsgpguild.example/locations</h2>
    <ul class="location-list">
      <li>Anaheim</li>
      <li>Burbank</li>
      <li>Camarillo</li>
      <li>Irvine</li>
      <li>Los Angeles (downtown)</li>
      <li>Long Beach</li>
      <li>Manhattan Beach</li>
      <li>Palmdale</li>
      <li>Palm Desert</li>
      <li>Pasadena</li>
      <li>Pomona</li>
      <li>Riverside</li>
      <li>Santa Clarita</li>
      <li>Santa Monica</li>
      <li>Temecula</li>
      <li>Woodland Hills</li>
    </ul>
  </section>
</div>
</body>
</html>
```